Plakate für Charity Unternehmen
Zielgruppe
Orno ist ein weltweit agierendes Charity Unternehmen.
Aufgabenstellung
Wir benötigen ein 'Plakat' Design, mit dem Zweck dieses Design als Banner, Sticker oder als Schild an unseren Projekten anzubringen. Das Schild soll in zwei verschiedenen Layouts geliefert werden.
1. Eine Art Blanko Version in der das Logo und das Motto eingearbeitet sind. Dieser Teil nimmt rund 1/3 des Plakats ein. Der Rest hat einen Freiraum auf dem wir Namen der Spender oder kooperative Charity Logos einsetzen können. Diese Version wird für Zusammenarbeit verwendet.
2. Eine zweite Version nimmt das gesamte Plakat ein, hier findet sich das Logo und das Motto welche das ganze Plakat einnehmen.
In beiden Fällen sollte die Aufteilung sauber und gut leserlich sein. Das Plakat wird in Auflösungen von bis zu 1,5m mal 1m gedruckt, sollte dementsprechend also die richtige Auflösung haben. Außerdem sollten Photoshop Datei möglichst mitgeliefert werden damit wir wenn nötig Namen und Logos einsetzen können.
Das einzuarbeitende Motto lautet:
إنما المؤمنون أخوة
Das Plakat sollte im Querformat sein und die Hintergrundfarbe sollte schwarz oder weiß sein.
Anbei befindet sich eine Beispieldatei wie das Plakat an den Projekten angebracht wird.

```html
<!DOCTYPE html>
<html lang="de">
<head>
<meta charset="utf-8">
<title>Korva – Plakat</title>
<link rel="stylesheet" href="https://fonts.googleapis.com/css2?family=Cinzel:wght@500&family=Lateef&display=swap">
<style>
  :root {
    --gold: #d2ae67;
    --blue: #1b75bc;
    --red: #d04a22;
    --ink: #141414;
    --paper: #ffffff;
  }
  html, body {
    margin: 0;
    padding: 0;
    overflow: hidden;
    background: var(--paper);
  }
  .poster {
    position: relative;
    width: 1200px;
    height: 848px;
    background: var(--paper);
    overflow: hidden;
  }
  .side-band {
    position: absolute;
    top: 204px;
    width: 330px;
  }
  .side-band--left { left: 0; }
  .side-band--right { left: 862px; width: 328px; }
  .side-band__gold { height: 59px; background: var(--gold); }
  .side-band__blue { height: 8px; margin-top: 11px; background: var(--blue); }
  .side-band__red { height: 15px; margin-top: 2px; background: var(--red); }

  .brand-mark {
    position: absolute;
    left: 500px;
    top: 100px;
    width: 190px;
    height: 190px;
    border-radius: 50%;
    background: var(--gold);
  }
  .brand-name {
    position: absolute;
    left: 0;
    width: 1200px;
    top: 352px;
    margin: 0;
    text-align: center;
    font-family: "Cinzel", "Times New Roman", serif;
    font-weight: 500;
    font-size: 118px;
    line-height: 1;
    letter-spacing: 2px;
    color: var(--ink);
  }
  .motto {
    position: absolute;
    left: 0;
    width: 1200px;
    top: 505px;
    margin: 0;
    text-align: center;
    direction: rtl;
    font-family: "Lateef", "Times New Roman", serif;
    font-size: 190px;
    line-height: 1.2;
    word-spacing: 20px;
    color: var(--gold);
  }
  .base-band {
    position: absolute;
    left: 0;
    top: 780px;
    width: 1200px;
    height: 68px;
    background: var(--gold);
  }
</style>
</head>
<body>
  <main class="poster">
    <div class="side-band side-band--left">
      <div class="side-band__gold"></div>
      <div class="side-band__blue"></div>
      <div class="side-band__red"></div>
    </div>
    <div class="side-band side-band--right">
      <div class="side-band__gold"></div>
      <div class="side-band__blue"></div>
      <div class="side-band__red"></div>
    </div>

    <div class="brand-mark" aria-hidden="true"></div>
    <h1 class="brand-name">KORVA</h1>

    <p class="motto" lang="ar">إنما المؤمنون أخوة</p>

    <div class="base-band"></div>
  </main>
</body>
</html>
```